VELVET ORBITS - BOOK COVER

I have written a book called VELVET ORBIT - HOW TO CLIMB PAST EVERY LIMIT TO THE TOP RUNG. I need a front cover design for the book. The book cover needs to be intriguing for someone to pick it up and read the first couple of pages. I want people to think about ACHIEVING SUCCESS when they read this book.
PLEASE LOOK AT THE ATTACHMENT. THANKS!

Target Market(s)

males, entrepreneurs, small business owners, salespeople, corporate executives

Industry/Entity Type

Business

Logo Text

VELVET ORBITS

Logo styles of interest
Emblem Logo
Abstract Logo
Font styles to use
Serif
Sans Serif

Colors
ec1f27
000000
959595
ffffff

Requirements
Must have
• It has to have a "hurricane" feel to it with hurricane colors.
Nice to have
• I open to your ideas
Should not have
• no other colors except red, black, gray, white.

```html
<!DOCTYPE html>
<html lang="en">
<head>
<meta charset="UTF-8">
<title>Velvet Orbit – Book Cover</title>
<link rel="stylesheet" href="https://fonts.googleapis.com/css2?family=Bebas+Neue&family=Montserrat:wght@300;500;700&display=swap">
<style>
  :root {
    --surround: #bcbdbf;
    --cover-black: #0b0909;
    --storm-dark: #1a1414;
    --storm-mid: #2e2624;
    --red: #ec1f27;
    --white: #ffffff;
    --gray: #c4c4c4;
  }
  * { margin: 0; padding: 0; box-sizing: border-box; }
  html, body {
    width: 907px; height: 1200px; overflow: hidden;
    background: var(--surround);
  }
  .book-cover {
    position: absolute; left: 100px; top: 100px;
    width: 707px; height: 1000px;
    background: var(--cover-black);
    overflow: hidden;
    font-family: 'Montserrat', sans-serif;
    text-align: center;
  }
  .storm-backdrop {
    position: absolute; inset: 0;
    background:
      radial-gradient(ellipse 55% 45% at 46% 55%, #3a302d 0%, var(--storm-mid) 30%, var(--storm-dark) 60%, transparent 85%),
      radial-gradient(ellipse 80% 70% at 40% 50%, #201a19 0%, var(--cover-black) 75%);
  }
  .title {
    position: absolute; left: 0; right: 0; top: 196px;
    font-family: 'Bebas Neue', sans-serif;
    font-weight: 400; line-height: 1;
  }
  .title-top { display: block; color: var(--white); font-size: 126px; letter-spacing: 1px; }
  .title-bottom { display: block; color: var(--red); font-size: 146px; letter-spacing: 1px; margin-top: -4px; }
  .brand {
    position: absolute; left: 0; right: 0; top: 536px;
    display: flex; flex-direction: column; align-items: center;
  }
  .brand-dot {
    width: 70px; height: 70px; border-radius: 50%;
    background: var(--gray); opacity: 0.85;
  }
  .brand-name {
    margin-top: 28px;
    color: var(--gray); font-weight: 500;
    font-size: 24px; letter-spacing: 1px;
  }
  .divider {
    position: absolute; left: 293px; top: 729px;
    width: 118px; height: 5px; background: var(--red);
  }
  .subtitle {
    position: absolute; left: 0; right: 0; top: 760px;
    color: var(--white); font-weight: 300;
    font-size: 31px; line-height: 45px; letter-spacing: 0.5px;
  }
  .author {
    position: absolute; left: 0; right: 0; top: 914px;
    color: var(--red); font-weight: 700;
    font-size: 17px; letter-spacing: 1.5px;
  }
</style>
</head>
<body>
  <main class="book-cover">
    <div class="storm-backdrop" role="img" aria-label="Dark satellite view of a swirling hurricane storm system"></div>
    <h1 class="title">
      <span class="title-top">VELVET</span>
      <span class="title-bottom">ORBIT</span>
    </h1>
    <div class="brand">
      <div class="brand-dot"></div>
      <div class="brand-name">VELVET ORBITS</div>
    </div>
    <div class="divider"></div>
    <p class="subtitle">HOW TO CLIMB PAST EVERY LIMIT<br>TO THE TOP RUNG</p>
    <p class="author">BY DALE MARWICK</p>
  </main>
</body>
</html>
```